LOLU Baby Massage Classes - flyer to make a difference

I need a single page flyer, preferably single page, to hand out to doctors, medical centres and parents. To also leave on counters of establishments.
It is to promote my baby massage classes. Mums can get together with other mums and book a 5 week course to learn and discover the many benefits of baby massage.
Benefits include: enhances bonding and attachment, understand non-verbal cues from your baby, helps with sleep patterns, help with immune system, increases vagal activity,relief from wind, colic or constipation to name some.

Baby age from birth to 12 months. Group classes or private sessions

I am a Professional Member and Certified by the Global Society of Newborn Touch (GSNT) GSNT Australia is Nationally Accredited and is endorsed by Crown Academy of Carers, the Southern Guild of Birth Attendants, The Southern Union of Daily Living Therapy Australia, The Southern Union of Bodywork Practitioner and is a full member of Wellmind Network Australia.

Class detail and availability contact is Petra Holm 0487 315 208 petra.joanne.holm@quillmail.example www.lolunewborntouch com.au facebook/comLOLUnewborntouch

My colour scheme is green and purple as you will see from my logo and website. I would like my flyer to be softer tones of either both colours or just one.

I will include some images you can choose from or show me any you think will fit in with baby massage. THANK YOU
Updates

Hi The size of my flyer is A6. Approx 150mms x 210mms and single sided. Thank you

Target Market(s)

mums and dads, groups, doctors, midwives

Industry/Entity Type

Medical

Font styles to use
Sans Serif

Colors
87d0c7
b09cc8

Requirements
Must have
• baby photo or photos, both my logo and the GSNT logo. The GSNT logo is to be small
• Baby Massage Classes (wording) is very important to catch the eye.
• Invitation to book a class or gather friends to book is next in importance
• Benefits is next
• The admin information ie.,membership, certification and endorsements are lesser and can be small.
• Contact information to be noticeable.
Nice to have
• If you have an idea, drawing or photo that would look better, please feel free to try it
Should not have
• should not be crowded with information all the same size

```html
<!DOCTYPE html>
<html lang="en">
<head>
<meta charset="utf-8">
<title>LOLU Baby Massage Classes</title>
<link rel="stylesheet" href="https://fonts.googleapis.com/css2?family=Baloo+2:wght@800&family=Open+Sans:ital,wght@0,400;0,600;0,700;1,400&display=swap">
<style>
  :root {
    --teal-deep: #19a497;
    --teal-soft: #87d0c7;
    --teal-panel: #7ecabf;
    --purple-deep: #7c3995;
    --purple-text: #83439c;
    --lavender: #b09cc8;
    --white: #ffffff;
    --page-bg: #ece9e4;
  }
  * { margin: 0; padding: 0; box-sizing: border-box; }
  html, body { width: 1200px; height: 1000px; overflow: hidden; background: var(--page-bg); }
  body { position: relative; font-family: "Open Sans", Arial, sans-serif; }

  .flyer {
    position: absolute; left: 30px; top: 215px; width: 1140px; height: 570px;
    background: var(--white); box-shadow: 0 4px 14px rgba(0,0,0,0.18); overflow: hidden;
  }
  .flyer-backdrop { position: absolute; inset: 0; }

  .brand { position: absolute; left: 62px; top: 40px; display: flex; align-items: center; gap: 14px; }
  .brand-dot { width: 86px; height: 86px; border-radius: 50%; background: var(--teal-deep); }
  .brand-name { font-family: "Open Sans", Arial, sans-serif; font-weight: 700; font-size: 44px; color: var(--teal-deep); letter-spacing: 1px; }

  .headline { position: absolute; left: 240px; top: 90px; width: 520px; text-align: center; }
  .headline svg { display: block; overflow: visible; }
  .headline text { font-family: "Baloo 2", "Arial Rounded MT Bold", sans-serif; font-weight: 800; text-anchor: middle; paint-order: stroke fill; stroke-linejoin: round; }
  .headline .book-now { fill: var(--teal-deep); stroke: var(--white); stroke-width: 7px; font-size: 50px; }
  .headline .title { fill: var(--lavender); stroke: var(--purple-deep); stroke-width: 9px; font-size: 64px; letter-spacing: -1px; }

  .baby-photo {
    position: absolute; right: 0; top: 0; width: 330px; height: 240px;
    background: radial-gradient(ellipse at 35% 55%, #e8c4b0 0%, #d9a995 35%, rgba(255,255,255,0) 72%),
                linear-gradient(120deg, #ffffff 0%, #f1e4dc 50%, #c9dff0 100%);
  }

  .body-copy { position: absolute; top: 312px; font-size: 16.5px; line-height: 21px; color: var(--purple-text); }
  .body-copy p + p { margin-top: 21px; }
  .body-copy strong { font-weight: 700; }
  .col-left { left: 50px; width: 380px; }
  .col-right { left: 452px; width: 390px; }
  .col-divider { position: absolute; left: 436px; top: 314px; width: 1.5px; height: 146px; background: var(--purple-text); }

  .credentials { position: absolute; left: 850px; top: 240px; width: 250px; color: var(--purple-text); }
  .credentials-heading { font-size: 10.5px; font-weight: 700; text-decoration: underline; color: #5d3573; }
  .credentials-badge { width: 52px; height: 36px; margin: 8px 0 8px 62px; border-radius: 8px; background: var(--lavender); }
  .credentials-text { font-size: 10.3px; font-style: italic; line-height: 15.5px; }

  .portrait {
    position: absolute; left: 1005px; top: 428px; width: 126px; height: 126px; border-radius: 50%;
    border: 5px solid var(--lavender);
    background: linear-gradient(160deg, #6e8f4c 0%, #9fb77a 45%, #8a5aa6 100%);
  }

  .contact { position: absolute; left: 50px; top: 489px; color: var(--white); }
  .contact-lead { font-size: 20px; font-weight: 700; white-space: nowrap; }
  .contact-lead .contact-name { font-size: 27px; font-weight: 600; }
  .contact-links { margin-top: 2px; font-size: 14px; font-weight: 600; display: flex; gap: 19px; }
</style>
</head>
<body>
  <main class="flyer">
    <svg class="flyer-backdrop" width="1140" height="570" viewBox="0 0 1140 570" aria-hidden="true">
      <path d="M5 115 Q 30 170 95 185" fill="none" stroke="var(--purple-deep)" stroke-width="9"/>
      <path d="M30 60 L30 555 L1110 555 L1110 150 C 900 170 760 200 560 250 C 380 290 200 290 30 60 Z" fill="var(--teal-panel)"/>
      <path d="M30 150 C 130 250 300 300 520 262 C 680 234 800 170 1110 140 L1110 175 C 820 190 700 250 520 280 C 300 318 120 270 30 175 Z" fill="var(--white)"/>
      <path d="M30 185 C 140 270 320 290 500 250 C 650 215 760 170 830 155" fill="none" stroke="var(--lavender)" stroke-width="16" stroke-linecap="round"/>
      <g fill="var(--teal-soft)" opacity="0.45">
        <circle cx="300" cy="330" r="85"/>
        <circle cx="720" cy="250" r="80"/>
        <circle cx="530" cy="430" r="90"/>
        <circle cx="860" cy="470" r="70"/>
      </g>
      <rect x="30" y="482" width="1080" height="58" fill="var(--teal-deep)"/>
      <rect x="30" y="25" width="1080" height="530" rx="18" fill="none" stroke="var(--teal-deep)" stroke-width="5"/>
    </svg>

    <div class="brand">
      <span class="brand-dot"></span>
      <span class="brand-name">lolu</span>
    </div>

    <div class="baby-photo" role="img" aria-label="Photo of a smiling baby lying on its back while a parent's hands massage its chest"></div>

    <h1 class="headline">
      <svg width="520" height="200" viewBox="0 0 520 200">
        <text class="book-now" x="260" y="50">BOOK NOW !!</text>
        <text class="title" x="260" y="118">BABY MASSAGE</text>
        <text class="title" x="260" y="175">CLASSES</text>
      </svg>
    </h1>

    <section class="body-copy col-left">
      <p>Mums can get together with other mums and book a <strong>5 week course</strong> to learn and discover the many benefits of baby massage.</p>
      <p><strong>BENEFITS INCLUDE: enhances bonding and attachment, understand non-verbal cues from your baby, helps with sleep patterns,</strong></p>
    </section>
    <div class="col-divider"></div>
    <section class="body-copy col-right">
      <p><strong>help with immune system, increases vagal activity, relief from wind, colic or constipation to name some.</strong></p>
      <p>Baby age from birth to 12 months.</p>
      <p><strong>JOIN GROUP CLASSES OR PRIVATE SESSIONS.</strong></p>
    </section>

    <aside class="credentials">
      <p class="credentials-heading">Professional Member &amp; Certified by</p>
      <div class="credentials-badge"></div>
      <p class="credentials-text">I am a Professional Member and Certified by the Global Society of Newborn Touch (GSNT). GSNT Australia is Nationally Accredited and is endorsed by Crown Academy of Carers, the Southern Guild of Birth Attendants, The Southern Union of Daily Living Therapy Australia, The Southern Union of Bodywork Practitioner and is a full member of Wellmind Network Australia.</p>
    </aside>

    <div class="portrait" role="img" aria-label="Portrait photo of instructor Petra Holm in a purple top"></div>

    <footer class="contact">
      <p class="contact-lead">Class Detail &amp; Availability Contact Is <span class="contact-name">: Petra Holm 0487 315 208</span></p>
      <p class="contact-links">
        <span>petra.joanne.holm@quillmail.example</span>
        <span>www.lolunewborntouch com.au</span>
        <span>facebook.com/LOLUnewborntouch</span>
      </p>
    </footer>
  </main>
</body>
</html>
```